Design einer ITK Unternehmensbroschüre  Grundlayouts mit Deckblatt gesucht
Design einer ITK Unternehmensbroschüre Grundlayouts mit Deckblatt gesucht
Zielgruppe
ITK Systemlösungen mit Schwerpunkt Kommunikationslösungen
Regionale kleine und mittelständische Unternehmen aus allen Branchen
Aufgabenstellung
Vorlage sollte für den Print und Email Versand vorbereitet sein (A4) als Unternehmensbroschüre, die Designlinie sollte bodenständig und innovativ ausgelegt sein.
Dieses Projekt ist als Projektstart zu bewerten und wird in ein eins zu eins Projekt mit erweiterten Budget fortgeführt.
Es soll dazu dienen ein Grundlayout mit Deckblatt zu erstellen um die richtige Linie / Partner zu finden.
Die Kreativität inklusive Aussuchen von passendem Bildmaterial wird vom Designer erwartet und durch Lizenzen im eins zu eins Projekt im Nachgang verrechnet.

```html
<!DOCTYPE html>
<html lang="de">
<head>
<meta charset="utf-8">
<title>Velunix – Telefonie-Lösungen</title>
<link href="https://fonts.googleapis.com/css2?family=Nunito+Sans:wght@300;400;600;700&display=swap" rel="stylesheet">
<style>
  :root {
    --stage: #e6e6ea;
    --paper: #ffffff;
    --paper-shade: #dcdde2;
    --navy: #1d2a3a;
    --text: #454a52;
    --rule: #9aa0a8;
    --photo-light: #e4e6ea;
    --photo-mid: #aeb3ba;
    --photo-dark: #2a2c30;
  }
  * { box-sizing: border-box; margin: 0; padding: 0; }
  html, body { width: 1200px; height: 848px; overflow: hidden; }
  body {
    background: var(--stage);
    font-family: "Nunito Sans", sans-serif;
    color: var(--text);
    position: relative;
  }
  .spread {
    position: absolute;
    left: 34px; top: 24px;
    width: 1132px; height: 800px;
    display: flex;
    box-shadow: 0 2px 10px rgba(0,0,0,.12);
  }
  .page {
    position: relative;
    width: 566px; height: 800px;
    overflow: hidden;
  }
  .page--left { background: var(--paper); }
  .page--right {
    background: linear-gradient(90deg, #f7f7f8 0%, var(--paper) 35%, #f3f3f5 70%, var(--paper-shade) 100%);
  }
  .page-title {
    position: absolute; left: 66px; top: 82px;
    font-size: 21px; font-weight: 700; letter-spacing: .2px;
    color: var(--navy);
  }
  .intro {
    position: absolute; left: 152px; top: 116px; width: 312px;
    font-size: 10.6px; line-height: 15px;
    text-align: justify; hyphens: auto;
  }
  .intro p + p { margin-top: 15px; }
  .hero-photo {
    position: absolute; left: 0; top: 420px;
    width: 566px; height: 380px;
    background:
      radial-gradient(ellipse at 30% 85%, var(--photo-dark) 0%, rgba(42,44,48,.85) 18%, rgba(42,44,48,0) 45%),
      radial-gradient(ellipse at 5% 45%, #3a3c41 0%, rgba(58,60,65,0) 30%),
      linear-gradient(180deg, var(--photo-mid) 0%, #c8ccd1 45%, var(--photo-light) 100%);
    clip-path: polygon(0 0, 372px 0, 370px 31px, 452px 0, 100% 0, 100% 100%, 0 100%);
  }
  .folio {
    position: absolute; bottom: 6px;
    width: 12px; height: 10px;
    font-size: 6px; line-height: 10px; text-align: center;
  }
  .folio--left { left: 0; background: var(--paper); color: var(--text); }
  .folio--right { right: 2px; background: var(--navy); color: #fff; }

  .brand {
    position: absolute; left: 386px; top: 52px;
    display: flex; align-items: center; gap: 7px;
    font-size: 24px; font-weight: 400; letter-spacing: 1px;
    color: var(--navy);
  }
  .brand-dot { width: 12px; height: 12px; border-radius: 50%; background: var(--navy); }

  .section-head {
    position: absolute;
    font-size: 10.8px; line-height: 13px; font-weight: 700;
    color: var(--navy);
  }
  .section-head--right { text-align: right; }
  .section-body {
    position: absolute;
    font-size: 9.9px; line-height: 14.3px;
    text-align: justify; hyphens: auto;
  }
  .section-body p + p { margin-top: 14.3px; }
  .connectors { position: absolute; left: 0; top: 0; }
</style>
</head>
<body>
  <main class="spread">
    <section class="page page--left">
      <h1 class="page-title">TELEFONIE-LÖSUNGEN</h1>
      <div class="intro">
        <p>Als klassischer Systemintegrator bieten wir unseren Kunden eine Vielzahl an hochmodernen sowie konservativen Telekommunikationslösungen an. Wir vereinen die klassische Telefonanlagenstruktur, wie man sie seit Jahrzehnten kennt in den neusten Produktversionen, mit den modernen Voice over IP Telefonanlagen. An einer Umrüstung auf ein modernes Telefonanlagensystem, egal ob bei Ihnen vor Ort oder ausgelagert in einem Rechenzentrum (Cloud/ Private Cloud), werden Sie in den nächsten Jahren nicht herumkommen.</p>
        <p>Wenn es mit der Umrüstung aufgrund der Carrier ISDN Abschaltung schnell gehen muss oder Sie aktuell keine neue Anlage kaufen, mieten oder leasen möchten, dann bieten wir Ihnen schlanke „Überbrückungslösungen“ in Form von Gateway Lösungen an. Diese Lösung spiegelt Ihre aktuelle IST-Situation auf die neue IP Welt, welche von den meisten Netzbetreibern vorausgesetzt wird.</p>
      </div>
      <div class="hero-photo" role="img" aria-label="Foto: Tischtelefon mit abgelegtem Hörer vor unscharfer Stadtkulisse, überlagert von VoIP-Netzwerksymbolen"></div>
      <span class="folio folio--left">06</span>
    </section>

    <section class="page page--right">
      <div class="brand"><span class="brand-dot"></span>Velunix</div>

      <svg class="connectors" width="566" height="800" aria-hidden="true">
        <g stroke="var(--rule)" stroke-width="0.8" fill="none">
          <path d="M224 79 V129"/>
          <path d="M300 167 H438 V187"/>
          <path d="M273 481 H122 V511"/>
          <path d="M404 568 V611"/>
        </g>
        <g fill="var(--rule)">
          <circle cx="224" cy="129" r="1.3"/>
          <circle cx="438" cy="187" r="1.3"/>
          <circle cx="122" cy="511" r="1.3"/>
          <circle cx="404" cy="611" r="1.3"/>
        </g>
      </svg>

      <h2 class="section-head section-head--right" style="right:347px; top:82px; width:200px;">Unified Communications und Collabpration [UCC]-Lösungen</h2>
      <div class="section-body" style="left:52px; top:134px; width:225px;">
        <p>Als Spezialist für Telefonielösungen bieten wir unseren Kunden an, die Agilität Ihres Unternehmens zu steigern. Durch den Einsatz von Unified Communications und Collaboration (UCC) -Lösungen verbinden Sie Ihre Teams und Informationen miteinander in Echtzeit und schaffen umfangreiche Möglichkeiten der Zusammenarbeit. Collaboration- und Kommunikationsfunktionen werden in Ihre Anwendungen und Geschäftsprozesse integriert und ermöglichen eine nahtlose, effiziente und gezielte Kommunikation. Diese hochmodernen Kommunikationslösungen ermöglichen eine höhere Effektivität sowie Steigerung der Kommunikation und entlastet viele alt eingewachsene Strukturen. Damit diese Transformation auch erfolgreich verläuft, bieten unsere Experten Ihnen einen sauberen Rollout Plan an und schwören Ihre Mitarbeiter auf persönlichen Schulungen auf das neue System ein.</p>
      </div>

      <h2 class="section-head section-head--right" style="right:293px; top:467px; width:200px;">Telefonanlagensysteme</h2>
      <div class="section-body" style="left:52px; top:515px; width:225px;">
        <p>Mit unseren namenhaften Technologiepartnern bieten wir Ihnen die klassische Telefonanlage, welche Sie seit Jahrzehnten kennen auf Basis von Voice over IP. Wir bedienen die modernsten und gängigsten Funktionen und Applikationen, um Ihr Geschäft weiterhin erreichbar und kommunikativ zu halten. Wir bieten Ihnen alle Vorteile einer Systemtelefonanlage, DECT Businesslösungen sowie einer modernen und flexiblen IP Telefonanlage mit der freien Auswahl an IP Endgeräten. Natürlich können alle unsere Lösungen bei Ihnen vor Ort oder im Rechenzentrum platziert werden. Unsere jahrelangen Branchenkenntnisse helfen Ihnen, die passende Lösung in Ihrem Unternehmen zu migrieren.</p>
      </div>

      <h2 class="section-head" style="left:300px; top:142px; width:205px;">ISDN &gt; Voice over IP Gatewaylösungen</h2>
      <div class="section-body" style="left:300px; top:190px; width:205px;">
        <p>Viele Kunden stehen vor der Herausforderung Ihre alten aber teilweise auch neueren Telefonanlagensysteme von ISDN auf Voice over IP umzurüsten. Viele Carrier haben bereits die herkömmlichen ISDN Anschlüsse abgeschaltet und viele Carrier haben das in den nächsten Jahren noch vor. Nicht selten trifft es einen unvorbereitet und man muss sich schnell entscheiden, da der Carrier mit Kündigung droht!</p>
        <p>Wir bieten unseren Kunden schlanke Gateway Lösungen, welche die aktuelle ISDN Struktur auf IP mittels einem Gateway Router spiegelt und dem aktuellen Carrier signalisiert, dass der Kunde IP spricht. Meistens sind die Kosten für eine solche Lösung weitaus geringer, als in eine Telefonanlage zu investieren, welche in zwei bis drei Jahren aufgrund von Softwareupdates oder möglicherweise End of Life Situationen seitens der Hersteller dann grundsätzlich geändert werden muss. Gerne zeigen wir Ihnen Ihre Möglichkeiten.</p>
      </div>

      <h2 class="section-head" style="left:409px; top:574px; width:110px;">Netzvermarktung - SIP TRUNK</h2>
      <div class="section-body" style="left:300px; top:614px; width:205px;">
        <p>Wir bieten kostengünstige und hochverfügbare IP Telefonie Tarife für den individuellen Kunden, welcher sich bei der herkömmlichen Carriern nicht gut aufgehoben fühlt. Die Velunix ist selbst Provider und bietet Ihren Kunden interessante Sprach- sowie -Datenlösungen an. Gerne erstellen wir Ihnen ein passendes Angebot.</p>
      </div>

      <span class="folio folio--right">07</span>
    </section>
  </main>
</body>
</html>
```